We need a small, simple graphic for the company newsletter. The topic of this issue is voting. As a company, we believe it is important to vote; therefore, we're going to explain the importance of voting, how to vote, when to vote, and how the company will be providing time off to vote. We would like the graphic to be simple (2-3 colors) and look like the sticker or pin you received after voting that says "I voted". We would like our company logo incorporated somehow, so be creative. It must contain our company color of blue (r 38, g 58, b 128). The company logo is attached, as well as some I voted stickers for reference

Requirements
Must have
• Use our company color of blue (r 38 g 58 b 128). Use the words "I Voted". Use the company font Bebas and/or Helvetica Neue. The background must be white as it will be incorporated into a newsletter document.
Nice to have
• Incorporate the company logo. American flag
Should not have
• fireworks, reference to 2020

```html
<!DOCTYPE html>
<html lang="en">
<head>
<meta charset="UTF-8">
<title>I Voted Sticker</title>
<link href="https://fonts.googleapis.com/css2?family=Bebas+Neue&family=Roboto:wght@700&display=swap" rel="stylesheet">
<style>
  :root {
    --brand-blue: #263a80;
    --flag-red: #ee2a27;
    --paper: #ffffff;
  }
  * { margin: 0; padding: 0; box-sizing: border-box; }
  html, body { width: 1200px; height: 1200px; overflow: hidden; background: var(--paper); }
  .sticker { position: relative; width: 1200px; height: 1200px; background: var(--paper); }
  .flag-frame { position: absolute; left: 0; top: 0; }
  .inner-frame {
    position: absolute; left: 199px; top: 199px; width: 802px; height: 802px;
    border: 5px solid var(--flag-red);
    display: flex; flex-direction: column; align-items: center; justify-content: center;
    gap: 70px;
  }
  .company-name {
    font-family: "Bebas Neue", sans-serif; font-size: 150px; line-height: 1;
    letter-spacing: 4px; color: var(--brand-blue); white-space: nowrap;
  }
  .voted-row { display: flex; align-items: center; gap: 28px; }
  .voted-i {
    font-family: "Roboto", sans-serif; font-weight: 700; font-size: 110px;
    line-height: 1; color: var(--brand-blue);
  }
  .voted-label {
    width: 480px; height: 140px; background: var(--brand-blue); color: var(--paper);
    font-family: "Roboto", sans-serif; font-weight: 700; font-size: 110px; line-height: 1;
    display: flex; align-items: center; justify-content: center;
  }
</style>
</head>
<body>
<div class="sticker">
  <svg class="flag-frame" width="1200" height="1200" viewBox="0 0 1200 1200">
    <g role="img" aria-label="Flag star field">
      <rect x="89" y="91" width="501" height="54" fill="#263a80"/>
      <rect x="89" y="91" width="84" height="413" fill="#263a80"/>
    </g>
    <g fill="#ee2a27">
      <rect x="590" y="91" width="521" height="54"/>
      <rect x="1027" y="187" width="84" height="65"/>
      <rect x="1027" y="312" width="84" height="65"/>
      <rect x="1027" y="434" width="84" height="65"/>
      <rect x="1027" y="554" width="84" height="65"/>
      <rect x="1027" y="677" width="84" height="65"/>
      <rect x="1027" y="797" width="84" height="65"/>
      <rect x="1027" y="919" width="84" height="65"/>
      <rect x="89" y="554" width="84" height="65"/>
      <rect x="89" y="677" width="84" height="65"/>
      <rect x="89" y="797" width="84" height="65"/>
      <rect x="89" y="919" width="84" height="65"/>
      <rect x="89" y="1042" width="1022" height="64"/>
    </g>
  </svg>

  <div class="inner-frame">
    <div class="company-name">HARLOW &amp; PIKE</div>
    <div class="voted-row">
      <span class="voted-i">I</span>
      <span class="voted-label">VOTED</span>
    </div>
  </div>
</div>
</body>
</html>
```